Business Card Design

Mortgage brokering company, also providing Commercial Finance, Car Finance and Insurance.

Target Market(s)

Home Buyers

Industry/Entity Type

Business

Contact Information for Business Card

All information required on business card is contained in the attachment. Design does not have to follow the style of the attachment.

```html
<!DOCTYPE html>
<html lang="en">
<head>
<meta charset="utf-8">
<title>Brightwell Mortgage Services – Business Card</title>
<link rel="stylesheet" href="https://fonts.googleapis.com/css2?family=Gentium+Book+Plus:wght@400;700&display=swap">
<style>
  :root {
    --bg: #e6e6e6;
    --card: #ffffff;
    --orange: #f0ab2e;
    --red: #e3261c;
    --ink: #3a3a3a;
    --white: #ffffff;
  }
  * { box-sizing: border-box; margin: 0; padding: 0; }
  html, body { width: 1200px; height: 926px; overflow: hidden; }
  body {
    background: var(--bg);
    font-family: "Gentium Book Plus", Georgia, serif;
    color: var(--ink);
    display: flex;
    align-items: center;
    justify-content: center;
    gap: 40px;
  }
  .card {
    position: relative;
    width: 540px;
    height: 330px;
    background: var(--card);
    box-shadow: 0 4px 14px rgba(0,0,0,0.18);
    overflow: hidden;
  }
  .brand {
    display: flex;
    align-items: center;
    gap: 8px;
    font-weight: 400;
    color: var(--ink);
  }
  .brand-dot {
    width: 16px; height: 16px;
    border-radius: 50%;
    background: var(--orange);
    flex: none;
  }
  /* Contact side */
  .contact .brand { position: absolute; top: 24px; left: 26px; font-size: 21px; }
  .person { position: absolute; top: 104px; left: 30px; }
  .person-name { font-size: 22px; font-weight: 400; }
  .person-name strong { font-weight: 700; }
  .person-role { color: var(--red); font-weight: 700; font-size: 13px; margin-top: 0; }
  .details { list-style: none; margin-top: 10px; font-size: 13px; line-height: 17px; }
  .details li { display: flex; align-items: center; gap: 9px; }
  .details svg { width: 11px; height: 11px; fill: var(--red); flex: none; }
  .contact .band {
    position: absolute; left: 0; right: 0; bottom: 18px;
    height: 22px; background: var(--orange);
  }
  /* Services side */
  .services .brand {
    position: absolute; top: 70px; left: 0; right: 0;
    flex-direction: column; gap: 10px;
    color: var(--red); font-size: 24px;
  }
  .services .brand-dot { width: 46px; height: 46px; }
  .services .band {
    position: absolute; left: 0; right: 0; bottom: 40px;
    height: 120px; background: var(--orange);
    display: flex; flex-direction: column; justify-content: center; align-items: center;
    color: var(--white); font-size: 17px; line-height: 22px;
  }
  .services .band strong { color: var(--red); font-weight: 700; }
</style>
</head>
<body>
  <section class="card contact">
    <div class="brand"><span class="brand-dot"></span>Brightwell Mortgage Services</div>
    <div class="person">
      <h1 class="person-name"><strong>Martin</strong> Hale</h1>
      <p class="person-role">Credit Representative</p>
      <ul class="details">
        <li><svg viewBox="0 0 12 12"><path d="M6 1 0.5 6H2v5h3V8h2v3h3V6h1.5z"/></svg>14 Coral Bay Road, Palm Beach, Qld 4221</li>
        <li><svg viewBox="0 0 12 12"><path d="M3 0h6a1 1 0 0 1 1 1v10a1 1 0 0 1-1 1H3a1 1 0 0 1-1-1V1a1 1 0 0 1 1-1zm0 2v7h6V2z"/></svg>0400 555 218</li>
        <li><svg viewBox="0 0 12 12"><path d="M1 4c0-2 2-3 5-3s5 1 5 3v1H8V4H4v1H1zm1 2h8l1 5H1z"/></svg>07 5550 1234</li>
        <li><svg viewBox="0 0 12 12"><circle cx="6" cy="6" r="5.5"/></svg>www.brightwellmortgage.com.au</li>
        <li><svg viewBox="0 0 12 12"><path d="M0 2h12v8H0zm1 1v.3l5 3.2 5-3.2V3z"/></svg>martin.hale@brightwellmortgage.com.au</li>
      </ul>
    </div>
    <div class="band"></div>
  </section>

  <section class="card services">
    <div class="brand"><span class="brand-dot"></span>Brightwell Mortgage Services</div>
    <div class="band">
      <p><strong>Residential</strong> – First Home, Refinance, Investment.</p>
      <p><strong>Asset Finance</strong> – Plant and Equipment. Motor Vehicle.</p>
      <p><strong>Insurance</strong> – Home, Contents, Car</p>
    </div>
  </section>
</body>
</html>
```